Word Page Templates x 5

1 x Letterhead Template with Header and Footer able to be printed to paper and pdf with non blurry resolution
- File attached looks ok on computer screen but does not print the same
- We are wanting it to print like it looks on the screen
- We are wanting it to print not fuzzy in resolution
- We are wanting the banner to be on the absolute edge of the page like it is on the computer screen
- We are needing to print this to paper and pdf with perfect resolution and colour

Please can someone help us!!

I have provided the logo files in our posession. If better resolutions are required please let us know.

We are also wanting 4 simple page templates to be setup in Landscape and Portrait orientation as well once we are happy with the letterhead that is provided samples have been provided
Updates

Hi all I have the vector files available now along with a Colour profile

Requirements
Must have
• Clear when printed on A4 Paper
Should not have
• Blurry images, Colour must be correct (same as Logo) - Please reference our website if need be ..... lomvira.com.au

```html
<!DOCTYPE html>
<html lang="en">
<head>
<meta charset="utf-8">
<title>Lomvira Pavement Services — Letterhead</title>
<link rel="stylesheet" href="https://fonts.googleapis.com/css2?family=Montserrat:wght@400;500;700;800&family=Open+Sans:wght@300;400&display=swap">
<style>
  :root {
    --backdrop: #eceeef;
    --paper: #ffffff;
    --band-top: #2f5987;
    --band-mid: #2f7f8a;
    --band-bottom: #3aa46b;
    --brand-blue: #3a5a8c;
    --brand-green: #2f9a55;
    --ink: #4a4d52;
    --band-ink: #ffffff;
  }
  * { box-sizing: border-box; margin: 0; padding: 0; }
  html, body { width: 1200px; height: 800px; overflow: hidden; }
  body { background: var(--backdrop); position: relative; font-family: "Open Sans", Arial, sans-serif; }

  .letterhead {
    position: absolute; left: 331px; top: 20px;
    width: 538px; height: 760px;
    background: var(--paper);
    box-shadow: 0 2px 14px rgba(0,0,0,.08);
    display: flex;
  }

  .side-band {
    width: 118px; height: 100%;
    background: linear-gradient(180deg, var(--band-top) 0%, var(--band-mid) 50%, var(--band-bottom) 100%);
    color: var(--band-ink);
    font-family: "Montserrat", Arial, sans-serif;
    padding: 66px 0 0 18px;
    position: relative;
  }
  .band-rule { width: 20px; height: 3px; background: var(--band-ink); margin-bottom: 8px; }
  .contact { font-size: 6.6px; line-height: 1.55; letter-spacing: .1px; }
  .contact b { font-weight: 700; }

  .affiliations { position: absolute; left: 18px; top: 440px; }
  .affiliations-title {
    font-size: 7.4px; font-weight: 500; letter-spacing: 1.2px;
    text-transform: uppercase; line-height: 1.6;
  }
  .partner-badges { margin-top: 24px; display: flex; flex-direction: column; gap: 38px; padding-left: 20px; }
  .badge { width: 34px; height: 22px; background: rgba(255,255,255,.85); border-radius: 3px; }
  .badge.round { width: 30px; height: 30px; border-radius: 50%; }

  .letter-body { flex: 1; position: relative; padding: 0 38px 0 60px; color: var(--ink); }

  .brand {
    position: absolute; right: 34px; top: 42px;
    display: flex; align-items: center; gap: 7px;
  }
  .brand-mark { width: 14px; height: 14px; background: var(--brand-green); }
  .brand-name {
    font-family: "Montserrat", Arial, sans-serif; font-weight: 800;
    font-size: 30px; letter-spacing: 1px; color: var(--brand-blue);
  }

  .salutation { margin-top: 198px; font-size: 9.6px; font-weight: 300; }
  .paragraph { margin-top: 22px; font-size: 9.6px; font-weight: 300; line-height: 2.65; }

  .sign-off { margin-top: 20px; text-align: right; font-size: 9.6px; font-weight: 300; }
  .signature { margin: 10px 0 0 auto; width: 120px; height: 44px; background: #f1f2f3; border-radius: 3px; }
</style>
</head>
<body>
  <article class="letterhead">
    <aside class="side-band">
      <div class="band-rule"></div>
      <p class="contact">
        <b>A.</b> PO Box 2318,<br>
        Marrowby QLD 4290<br>
        <b>P.</b> 07 5500 1872<br>
        <b>E.</b> admin@lomvira.com.au<br>
        <b>W.</b> lomvira.com.au
      </p>

      <section class="affiliations">
        <div class="band-rule"></div>
        <p class="affiliations-title">Lomvira<br>Pavement<br>Services are<br>proudly<br>affiliated:</p>
        <div class="partner-badges">
          <div class="badge" role="img" aria-label="Partner association badge"></div>
          <div class="badge round" role="img" aria-label="Industry association member badge"></div>
          <div class="badge round" role="img" aria-label="Airports association badge"></div>
          <div class="badge" role="img" aria-label="Line removal partner badge"></div>
        </div>
      </section>
    </aside>

    <main class="letter-body">
      <header class="brand">
        <span class="brand-mark"></span>
        <span class="brand-name">LOMVIRA</span>
      </header>

      <p class="salutation">Dear Mrs Halvorsen,</p>

      <p class="paragraph">The quick, brown fox jumps over a lazy dog. DJs flock by when VTQ ax quiz prog. Junk VTQ quiz graced by fox whelps. Bawds jog, flick quartz, vex nymphs. Waltz, bad nymph, for quick jigs vex! Fox nymphs grab quick-jived waltz. Brick quiz whangs jumpy veldt fox. Bright vixens jump; dozy fowl quack. Quick wafting zephyrs vex bold Jim. Quick zephyrs blow, vexing daft Jim.</p>

      <p class="paragraph">Sex-charged fop blew my junk TV quiz. How quickly daft jumping zebras vex. Two driven jocks help fax my big quiz. Quick, Baz, get my woven flax jodhpurs! "Now fax quiz Jack!" my brave ghost pled. Five quacking zephyrs jolt my wax bed. Flummoxed by job, kvetching W. zaps Iraq. Cozy sphinx waves quart jug of bad milk. A very bad quack might jinx zippy fowls.</p>

      <p class="paragraph">Few quips galvanized the mock jury box. Quick brown dogs jump over the lazy fox. The jay, pig, fox, zebra, and my wolves quack! Blowzy red vixens fight for a quick jump. Jorvan Pellek was gazed by VTQ for luck. A wizard's job is to vex chumps quickly in fog. Watch "Quizbox!", Alder Trevane's fun TV quiz game. Woven silk pyjamas exchanged for blue quartz.</p>

      <p class="sign-off">Best Regards</p>
      <div class="signature" role="img" aria-label="Handwritten signature"></div>
    </main>
  </article>
</body>
</html>
```